PowerPoint Design Project

Design Brief
Corvanta is updating its stationary templates to reflect the company’s position as market leader in smart-location based solutions.
Using the existing Corvanta logo and corporate colours, create an engaging and visually appealing PowerPoint presentation template identity that works when printed on A4 and US Letter sized paper.
The successful designs will complement the current look and feel of the Corvanta website (www.corvanta-example.net) and communicate that Corvanta is a dynamic and modern technology company that is at the cutting edge of innovation.
Corvanta Brand
Corvanta stands for Precision Location Technology. The brand represents both a unique, highly innovative platform product and a mature consulting and support organisation dedicated to delivering solutions to blue-chip customer problems. The orange colour implies creativity while blue evokes trust and a rational approach. “Ubi” is Latin and means “where”, so the brand directly addresses the focus of the company: location. “Sense” can mean that we have sensing technology to support our precision location aware applications and solutions, but also that we make sensible use of location data to improve customer processes.
Corvanta Corporate Profile
Corvanta is a market leader of location-based Smart Factory Solutions which enables companies to optimise their business processes. By keeping track of key assets, Corvanta solutions bring clarity to complex operations in industries while also improving quality and reliability. Corvanta uses a unique combination of advancefd industry knowledge and an experienced team to deliver effective and superior solutions that offer unprecedented visibility, control and accuracy, delivering time and cost savings. Corvanta solutions are easy to implement and flexible to a particular business’s needs, no matter which area of the globe they operate in.
Corvanta offers two location-oriented products; RTLS (Real-time Location Solutions) and Geospatial Systems and operates in a number of industries ranging from manufacturing and utilities to telecommunications and is used by a number of blue chip customers across the world, such as KLT, Skyvane, Groundmole, Fenwick Power, RAL and Nordische Fernmelde.
Corvanta Corporate Colours
Orange:
Pantone 021C
R: 237 / G: 110 / B: 0
C: 0 / M: 53 / Y: 100 / K: 0
Hex #ED6E00
Dark Blue:
Pantone 662C
R: 15 / G: 31 / B: 122
C: 100 / M: 71 / Y: 0 / K:0
Hex #0F1F7A
Light Blue:
Pantone 300C
R: 0 / G: 110 / B: 199
C: 100 / M: 44 / Y: 0 / K:0
Hex #006EC7
Corvanta Corporate Fonts
The preferred font is Tahoma for Title, Topics and Print. In certain situations, Arial is an acceptable alternative.
Target Market(s)
Manufacturing industry, Automotive and Aerospace
Industry/Entity Type
Telecommunications
Look and feel

```html
<!DOCTYPE html>
<html lang="en">
<head>
<meta charset="utf-8">
<title>Corvanta — Thank You</title>
<link rel="stylesheet" href="https://fonts.googleapis.com/css2?family=Open+Sans:wght@400;600;700;800&display=swap">
<style>
  :root {
    --cream-top: #efede2;
    --cream-bottom: #f8f5ee;
    --charcoal: #333037;
    --charcoal-deep: #2b282e;
    --rule: #4a474c;
    --title-dark: #3a3a3c;
    --accent-yellow: #fbb800;
    --band-orange: #ffad00;
    --brand-blue: #1f5aa8;
    --brand-orange: #ed8a00;
    --contact-text: #f2f2f2;
  }
  * { margin: 0; padding: 0; box-sizing: border-box; }
  html, body {
    width: 1200px;
    height: 900px;
    overflow: hidden;
    background: var(--charcoal);
  }
  .slide {
    position: relative;
    width: 1200px;
    height: 900px;
    font-family: "Open Sans", Tahoma, Arial, sans-serif;
    overflow: hidden;
  }
  .slide__upper {
    position: absolute;
    left: 0; top: 0;
    width: 1200px; height: 495px;
    background: linear-gradient(180deg, var(--cream-top) 0%, var(--cream-bottom) 100%);
  }
  .slide__rule {
    position: absolute;
    left: 0; top: 495px;
    width: 1200px; height: 2px;
    background: var(--rule);
  }
  .slide__lower {
    position: absolute;
    left: 0; top: 497px;
    width: 1200px; height: 378px;
    background: radial-gradient(ellipse at 55% 85%, #3a373e 0%, var(--charcoal) 45%, var(--charcoal-deep) 100%);
  }
  .slide__footer-band {
    position: absolute;
    left: 0; top: 875px;
    width: 1200px; height: 25px;
    background: var(--band-orange);
  }
  .slide__title {
    position: absolute;
    left: 53px; top: 192px;
    font-size: 86px;
    font-weight: 800;
    letter-spacing: -1px;
    line-height: 1;
    color: var(--title-dark);
  }
  .slide__title-accent { color: var(--accent-yellow); }
  .brand {
    position: absolute;
    left: 27px; top: 811px;
    display: flex;
    align-items: center;
    gap: 8px;
  }
  .brand__mark {
    width: 30px; height: 30px;
    border-radius: 50%;
    background: var(--brand-orange);
  }
  .brand__name {
    font-size: 29px;
    font-weight: 600;
    color: var(--brand-blue);
    line-height: 1;
  }
  .contact {
    position: absolute;
    left: 892px; top: 770px;
    font-size: 13px;
    line-height: 18px;
    color: var(--contact-text);
  }
  .contact__heading {
    font-weight: 700;
    color: var(--accent-yellow);
  }
</style>
</head>
<body>
  <main class="slide">
    <div class="slide__upper"></div>
    <div class="slide__rule"></div>
    <div class="slide__lower"></div>
    <div class="slide__footer-band"></div>

    <h1 class="slide__title">THANK <span class="slide__title-accent">YOU</span></h1>

    <div class="brand">
      <span class="brand__mark"></span>
      <span class="brand__name">Corvanta</span>
    </div>

    <address class="contact" style="font-style: normal;">
      <p class="contact__heading">Contact Us</p>
      <p>Lorem ipsum dolor, 03663, State, Country</p>
      <p>P.&nbsp; 281 555 0172/ hello@corvanta-example.net</p>
    </address>
  </main>
</body>
</html>
```